HVAC company business card design

We need a business card design for a HVAC company. The design must look professional. Both sides will be used. The total data to be on the business card is
Name
Position
Email
Direct Phone/Moile Phone
Company Contacts /Address, Phone, Fax, web)
All data will be submit once the design is confirmed. For generic purposes use;
Emre Toksoy
Managing Director
+902324815263 (Mobile)
4712 Sokak No: 9 KBSE Yenikent IZMIR TURKEY
Tel: +902324815263 Fax : +902324815269
www.luvon.com.tr

Target Market(s)

HVAC

Industry/Entity Type

Business

Contact Information for Business Card

The total data to be on the business card is
Name
Position
Email
Direct Phone/Moile Phone
Emre Toksoy
Managing Director
+902324815263 (Mobile)
www.luvon.com.tr
The BC will use both sides of the card. The front will include the full logo and the details for the business card holder. The business card can be divided into vertical/horizontal or to a special shape. The common data like the company address/phone/fax should be indicated elsewehere. The back can contain some part or the whole logo and must contain the web address.

Font styles to use
Serif
Sans Serif

Colors
0355a3
cfdfed

Requirements
Should not have
• Please be careful with the fonts, it shouldnt be too small or too big and must not interfere with the logo fonts. If you need to use a curvy shape please do not use as the logo is already curvy or use the curves from the logo (if it looks good, otherwise forget it)
• We are not in favor of pictograms, only if they are perfect use them.

```html
<!DOCTYPE html>
<html lang="en">
<head>
<meta charset="utf-8">
<title>LUVON business card</title>
<link href="https://fonts.googleapis.com/css2?family=Open+Sans:wght@400;600;700&display=swap" rel="stylesheet">
<style>
  :root {
    --bg-light: #c4c4c4;
    --bg-dark: #7d7d7d;
    --card-white: #ffffff;
    --card-fade: #e9e9ea;
    --navy-light: #5b6480;
    --navy-dark: #353d55;
    --ink: #4a5064;
    --brand-blue: #3b6fc4;
    --brand-pale: #cfdfed;
    --rule: #b9c6dc;
  }
  * { margin: 0; padding: 0; box-sizing: border-box; }
  html, body { width: 1200px; height: 900px; overflow: hidden; }
  body {
    font-family: "Open Sans", sans-serif;
    background: radial-gradient(ellipse at 45% 40%, var(--bg-light) 0%, var(--bg-dark) 100%);
    position: relative;
  }
  .card {
    position: absolute;
    width: 600px;
    height: 340px;
    border-radius: 18px;
    box-shadow: 0 6px 18px rgba(0,0,0,0.25);
    overflow: hidden;
  }
  /* Front */
  .card-front {
    left: 170px; top: 100px;
    background: linear-gradient(100deg, var(--card-white) 0%, var(--card-white) 40%, var(--card-fade) 100%);
  }
  .brand-front {
    position: absolute; left: 60px; top: 60px;
    display: flex; align-items: center; gap: 16px;
  }
  .brand-dot {
    width: 56px; height: 56px; border-radius: 50%;
    background: var(--brand-blue);
  }
  .brand-name {
    font-weight: 700; font-size: 54px; letter-spacing: 4px;
    color: var(--ink); line-height: 1;
  }
  .accent-rule {
    position: absolute; left: 330px; top: 208px;
    width: 270px; height: 1px; background: var(--rule);
  }
  .holder {
    position: absolute; left: 185px; top: 190px;
  }
  .holder-name { font-weight: 700; font-size: 24px; color: var(--ink); }
  .holder-role { font-size: 14px; color: var(--brand-blue); margin-top: 2px; }
  .contacts {
    position: absolute; left: 185px; top: 262px;
    display: grid; grid-template-columns: 172px auto; row-gap: 6px; column-gap: 0;
    font-size: 14px; color: var(--brand-blue);
  }
  .contact { display: flex; align-items: center; gap: 6px; white-space: nowrap; }
  .contact svg { width: 13px; height: 13px; fill: var(--ink); flex: none; }
  .address {
    position: absolute; left: 195px; top: 312px;
    font-size: 14px; color: var(--brand-blue); white-space: nowrap;
  }
  .contacts-shifted { top: 236px; left: 357px; grid-template-columns: auto; }
  /* Back */
  .card-back {
    left: 420px; top: 480px;
    background: linear-gradient(100deg, var(--navy-light) 0%, var(--navy-dark) 100%);
  }
  .brand-back {
    position: absolute; left: 150px; top: 110px;
    display: flex; align-items: center; gap: 18px;
  }
  .brand-back .brand-name { color: var(--brand-pale); font-size: 60px; }
  .web {
    position: absolute; left: 0; right: 0; top: 262px;
    text-align: center; font-size: 13px; letter-spacing: 5px;
    color: var(--brand-blue);
  }
</style>
</head>
<body>

<section class="card card-front">
  <div class="brand-front">
    <span class="brand-dot"></span>
    <span class="brand-name">LUVON</span>
  </div>
  <div class="accent-rule"></div>
  <div class="holder">
    <div class="holder-name">Emre Toksoy</div>
    <div class="holder-role">Managing Director</div>
  </div>
  <div class="contacts">
    <div class="contact">
      <svg viewBox="0 0 16 16"><rect x="4" y="1" width="8" height="14" rx="1.5"/></svg>
      +902324815263
    </div>
    <div class="contact">
      <svg viewBox="0 0 16 16"><rect x="1" y="3" width="14" height="10" rx="1"/><path d="M1 3l7 6 7-6" fill="none" stroke="#fff" stroke-width="1.4"/></svg>
      emre_toksoy@luvon.com.tr
    </div>
    <div class="contact">
      <svg viewBox="0 0 16 16"><rect x="0.5" y="0.5" width="15" height="15" rx="3"/><path d="M5 3.5l2 2-1 1.5c.7 1.5 1.5 2.3 3 3l1.5-1 2 2-1.3 1.5C7.5 12 4 8.5 3.5 4.8z" fill="#fff"/></svg>
      +902324815269
    </div>
  </div>
  <div class="contacts contacts-shifted">
    <div class="contact">
      <svg viewBox="0 0 16 16"><rect x="1" y="5" width="14" height="9" rx="1"/><rect x="4" y="1" width="8" height="5" fill="none" stroke="currentColor"/></svg>
      +902324815263
    </div>
  </div>
  <div class="address">4712 Sokak No: 9 KBSE Yenikent IZMIR TURKEY</div>
</section>

<section class="card card-back">
  <div class="brand-back">
    <span class="brand-dot"></span>
    <span class="brand-name">LUVON</span>
  </div>
  <div class="web">www.luvon.com.tr</div>
</section>

</body>
</html>
```